Elegant and modern Wedding Photography brochure

My existing brochure (attached) needs a major facelift. This is one of the main selling tools - it gets emailed to my clients when they make an equiry on what packages i offer and it is printed out and walked through at our first meeting. This brochure is as critical as my website - it needs to sing!

I'm looking for an eye-catching design that says:
Elegant
Modern
Clean
Crisp
Not cutesy or lovey-dovey thanks - we are more sophisticated and professional than that.

Update images to some of the latest weddings I've shot also. Let me know files and resolution you need. I've enabled right-click to download images on my site for a limited time. Please note that I retain copyright and will pursue any breeches.

Http://www.carlathornbey.com/Melbourne-wedding-photography
Updates

Thanks for all of your designs! Will take a few days to decide.

Target Market(s)

Australian Women aged 24-44

Industry/Entity Type

Wedding

Font styles to use
Other font styles liked:
• Century Gothic

Requirements
Must have
• Easy to print - does not have to be 6 A4 pages like the existing brochure
Nice to have
• Some full page images - The photos are supposed to be the hero here :-)
Should not have
• Not cutesy or lovey-dovey thanks - we are more sophisticated and professional than that.

No black backgrounds, I prefer a white thanks

No images in organic shaped boxes (like the rectangles in the logo - no thanks).
Keep the lines straight and sharp

```html
<!DOCTYPE html>
<html lang="en">
<head>
<meta charset="utf-8">
<title>Elena Marlowe – Wedding Packages Brochure</title>
<link href="https://fonts.googleapis.com/css2?family=Questrial&display=swap" rel="stylesheet">
<style>
  :root {
    --canvas: #ebebeb;
    --paper: #f7f7f6;
    --ink: #6d6d6d;
    --rule: #dcdcdc;
    --teal: #1f9a86;
    --peach: #e8aa92;
    --orchid: #a06ea3;
    --orchid-band: rgba(165, 118, 168, 0.92);
    --brand: #8c2f8d;
    --photo-garden: linear-gradient(160deg, #b9ad92 0%, #8f8468 45%, #6e6452 100%);
    --photo-barn: linear-gradient(180deg, #e9e8df 0%, #c9cabd 55%, #7f8670 100%);
    --photo-veil: linear-gradient(150deg, #f1e3d8 0%, #d9b8a6 55%, #b58e7d 100%);
    --photo-roses: linear-gradient(180deg, #e9d6cf 0%, #d9b6b0 50%, #b5958d 100%);
  }
  * { box-sizing: border-box; margin: 0; padding: 0; }
  html, body { width: 1200px; height: 1000px; overflow: hidden; }
  body {
    background: var(--canvas);
    font-family: "Questrial", "Century Gothic", sans-serif;
    color: var(--ink);
    position: relative;
  }

  .spread {
    position: absolute;
    display: flex;
    background: var(--paper);
    box-shadow: 0 6px 18px rgba(0,0,0,0.12);
  }
  .page { position: relative; flex: 1; display: flex; overflow: hidden; }
  .page + .page { border-left: 1px solid #e2e2e2; }
  .photo { height: 100%; }

  .spread--tiers { left: 228px; top: 40px; width: 766px; height: 276px; }
  .spread--tiers .photo { width: 168px; flex: none; }
  .photo--barn { background: var(--photo-barn); }
  .photo--veil { background: var(--photo-veil); }

  .package { flex: 1; padding: 16px 16px 0 18px; position: relative; }
  .package__title { font-size: 17px; font-weight: 400; padding-bottom: 8px; border-bottom: 1px solid var(--rule); margin-bottom: 8px; }
  .package--platinum .package__title { color: var(--teal); }
  .package--gold .package__title { color: var(--peach); }
  .package--signature .package__title { color: var(--orchid); }

  .inclusions { list-style: none; font-size: 5.4px; line-height: 1.35; }
  .inclusions li { position: relative; padding-left: 11px; margin-bottom: 5px; }
  .inclusions li::before {
    content: ""; position: absolute; left: 0; top: 0;
    width: 5px; height: 5px; border: 0.8px solid #9c9c9c;
  }
  .inclusions li::after {
    content: ""; position: absolute; left: 2px; top: -1px;
    width: 2px; height: 4px; border: solid var(--orchid);
    border-width: 0 1px 1px 0; transform: rotate(40deg);
  }

  .price {
    position: absolute; border-radius: 50%;
    display: flex; flex-direction: column; align-items: center; justify-content: center;
    color: #fff; text-align: center;
  }
  .spread--tiers .price { left: 18px; bottom: 30px; width: 64px; height: 64px; font-size: 8px; }
  .price__value { font-size: 0.8em; opacity: 0.85; margin-top: 2px; }
  .package--platinum .price { background: var(--teal); }
  .package--gold .price { background: var(--peach); }
  .package--signature .price { background: var(--orchid); }

  .brand {
    position: absolute; left: 300px; top: 440px;
    display: flex; align-items: center; gap: 10px;
    font-size: 26px; color: var(--brand);
  }
  .brand__mark { width: 14px; height: 14px; background: var(--brand); }

  .spread--opening { left: 36px; top: 500px; width: 1128px; height: 450px; }
  .page--cover { flex: none; width: 600px; }
  .photo--embrace { width: 100%; background: var(--photo-garden); }
  .cover-band {
    position: absolute; left: 0; top: 250px;
    padding: 8px 28px 8px 30px;
    background: var(--orchid-band); color: #fff;
    font-size: 26px; font-weight: 400; letter-spacing: 0.5px;
  }
  .photo--roses { width: 120px; flex: none; }
  .page--signature .photo--roses { background: var(--photo-roses); }
  .package--signature { padding: 28px 40px 0 36px; }
  .package--signature .package__title { font-size: 28px; padding-bottom: 10px; margin-bottom: 12px; }
  .package--signature .inclusions { font-size: 10px; }
  .package--signature .inclusions li { padding-left: 18px; margin-bottom: 6px; }
  .package--signature .inclusions li::before { width: 9px; height: 9px; top: 1px; }
  .package--signature .inclusions li::after { left: 3px; top: -1px; width: 4px; height: 8px; border-width: 0 1.5px 1.5px 0; }
  .package--signature .price { left: 36px; bottom: 18px; width: 100px; height: 100px; font-size: 12px; }
</style>
</head>
<body>

  <section class="spread spread--tiers">
    <article class="page">
      <div class="photo photo--barn" role="img" aria-label="Bride and groom standing before white barn doors"></div>
      <div class="package package--platinum">
        <h2 class="package__title">Platinum Package</h2>
        <ul class="inclusions">
          <li>Up to 8 hrs of coverage</li>
          <li>Signature Grand (A3) Album with Lay-flat 300gsm pages, frosted page, choice of premium linen or leather cover, presentation box, name embossing, up to 52 pages</li>
          <li>Custom Thank-you Cards with envelopes (50)</li>
          <li>Client for life (no sitting fees)</li>
          <li>Second photographer</li>
          <li>Fusion Slideshow (stills + moving images)</li>
          <li>Pre-wedding Shoot</li>
          <li>Web Gallery (online for 6 weeks) &amp; Social media</li>
          <li>High Resolution Digital Negatives*</li>
        </ul>
        <div class="price"><span>Price: $2300</span><span class="price__value">($3440 value)</span></div>
      </div>
    </article>
    <article class="page">
      <div class="photo photo--veil" role="img" aria-label="Bride adjusting a birdcage veil"></div>
      <div class="package package--gold">
        <h2 class="package__title">Gold Package</h2>
        <ul class="inclusions">
          <li>Up to 8 hrs of coverage</li>
          <li>Signature Grand (A3) Album with Lay-flat 300gsm pages, frosted page, choice of premium linen or leather cover, presentation box, name embossing, up to 52 pages</li>
          <li>Custom Thank-you Cards with envelopes (50)</li>
          <li>Client for life (no sitting fees)</li>
          <li>Second photographer</li>
          <li>Fusion Slideshow (stills + moving images)</li>
          <li>Pre-wedding Shoot</li>
          <li>Web Gallery (online for 6 weeks) &amp; Social media</li>
          <li>High Resolution Digital Negatives*</li>
        </ul>
        <div class="price"><span>Price: $1650</span><span class="price__value">($2080 value)</span></div>
      </div>
    </article>
  </section>

  <div class="brand"><span class="brand__mark"></span><span class="brand__name">Elena Marlowe</span></div>

  <section class="spread spread--opening">
    <article class="page page--cover">
      <div class="photo photo--embrace" role="img" aria-label="Bride and groom embracing in a garden, groom holding a bouquet"></div>
      <h1 class="cover-band">Wedding Packages</h1>
    </article>
    <article class="page page--signature">
      <div class="photo photo--roses" role="img" aria-label="Pale pink roses in a vase"></div>
      <div class="package package--signature">
        <h2 class="package__title">Signature Package</h2>
        <ul class="inclusions">
          <li>Up to 8 hrs of coverage</li>
          <li>Signature Grand (A3) Album with Lay-flat 300gsm pages, frosted page, choice of premium linen or leather cover, presentation box, name embossing, up to 52 pages</li>
          <li>Custom Thank-you Cards with envelopes (50)</li>
          <li>Client for life (no sitting fees)</li>
          <li>Second photographer</li>
          <li>Fusion Slideshow (stills + moving images)</li>
          <li>Pre-wedding Shoot</li>
          <li>Web Gallery (online for 6 weeks) &amp; Social media</li>
          <li>High Resolution Digital Negatives*</li>
        </ul>
        <div class="price"><span>Price: $3650</span><span class="price__value">($5340 value)</span></div>
      </div>
    </article>
  </section>

</body>
</html>
```